Urgent - brand new business card for a startup technical advisory and incubation business in Sydney

We need a brand new business card design for BrightForge. We are a startup technical advisory and incubation business based in Sydney Australia. We work with entrepreneurs and innovators to help rapidly and efficiently turn their ideas into reality and to ensure they have the technical platform required for growth.

Our name is partly inspired by our love of lean product development methods and the lean startup movement.

We would like clean, uncluttered designs that feature our two logo colours and communicate a professional but creative, in-touch and entrepreneurial business.

PLEASE SEE MUST HAVE PRIORITIES FOR DRAFT CONTACT INFORMATION AND OTHER DESIRED TEXT ON CARD.
Updates

We have now updated the brief to include draft business card contact information and also some additional desired text to feature on the card design.    Please review the Must Have priorities.

Also final updated source files for the horizontal and vertical versions have now been uploaded and should be used for any designs.

Thanks!

Target Market(s)

Entrepeneurs, innovators, startup investors looking for a strong product development partner

Industry/Entity Type

Business

Requirements
Must have
• Feature our two logo colours
Be a relatively clean, pared back overall design - quite minimalist

Updated source files (AI) for vertical and horizontal layouts attached.

Draft contact information for business card:
Tom Harcourt
Founder & CTO
Phone: +61 427 555123
Email: xxxx@brightforge.example
Skype: xxxxxharcourt
Twitter: tharcourt

www.brightforge.example

We would also like the overall design to include the phrase "You have great ideas. Let us make them happen." (probably in a reasonably subtle way)

Nice to have
• Inspire me! Double-sided designs are fine with logo, phrase, (URL?) on one side and contact details on other (+ any other design elements)

Logo on business card can be either with lightbulb above the wording as per example here or to the left of the BrightForge wording - both layouts in files provided.
Should not have
• Shouldn't look like a Pendrel Suite business card template :-)

```html
<!DOCTYPE html>
<html lang="en">
<head>
<meta charset="utf-8">
<title>BrightForge business card</title>
<link rel="stylesheet" href="https://fonts.googleapis.com/css2?family=Roboto+Condensed:wght@700&family=Cabin+Sketch:wght@700&family=Architects+Daughter&display=swap">
<style>
  :root {
    --brand-blue: #1ea0dc;
    --brand-ink: #26303d;
    --card-white: #fbfbfb;
    --card-edge: #e4e4e4;
    --stage: #ecedef;
    --muted-ink: #3a4452;
  }
  * { margin: 0; padding: 0; box-sizing: border-box; }
  html, body {
    width: 1200px;
    height: 900px;
    overflow: hidden;
    background: var(--stage);
  }
  .canvas {
    width: 1200px;
    height: 900px;
    display: flex;
    flex-direction: column;
    align-items: center;
    justify-content: center;
    gap: 40px;
  }
  .card {
    position: relative;
    width: 700px;
    height: 400px;
    border-radius: 28px;
    overflow: hidden;
    background: linear-gradient(160deg, #ffffff 0%, var(--card-white) 60%, #f1f1f1 100%);
    border: 1px solid var(--card-edge);
    box-shadow: 0 6px 18px rgba(0,0,0,0.10);
  }
  .wordmark {
    display: flex;
    align-items: center;
    gap: 14px;
    font-family: "Roboto Condensed", "Arial Narrow", sans-serif;
    font-weight: 700;
    color: var(--brand-blue);
    letter-spacing: -1px;
    line-height: 1;
    white-space: nowrap;
  }
  .wordmark-dot {
    border-radius: 50%;
    background: var(--brand-ink);
  }
  .card-front .wordmark {
    position: absolute;
    left: 50%;
    top: 50%;
    transform: translate(-50%, -50%);
    font-size: 84px;
  }
  .card-front .wordmark-dot { width: 62px; height: 62px; }
  .card-back .wordmark {
    position: absolute;
    left: 50%;
    top: 52px;
    transform: translateX(-50%);
    font-size: 54px;
  }
  .card-back .wordmark-dot { width: 42px; height: 42px; }
  .person {
    position: absolute;
    left: 56px;
    top: 250px;
  }
  .person-name {
    font-family: "Cabin Sketch", cursive;
    font-weight: 700;
    font-size: 32px;
    letter-spacing: 2px;
    text-transform: uppercase;
    color: var(--muted-ink);
    white-space: nowrap;
  }
  .person-role {
    margin: 8px 0 0 44px;
    font-family: "Architects Daughter", cursive;
    font-size: 14px;
    letter-spacing: 1px;
    text-transform: uppercase;
    color: var(--brand-blue);
  }
  .contact {
    position: absolute;
    left: 372px;
    top: 160px;
    height: 140px;
    padding: 4px 0 4px 20px;
    border-left: 2px solid var(--brand-blue);
    list-style: none;
    display: flex;
    flex-direction: column;
    justify-content: space-between;
  }
  .contact-item {
    display: flex;
    align-items: center;
    gap: 14px;
    font-family: "Architects Daughter", cursive;
    font-size: 13px;
    letter-spacing: 0;
    text-transform: uppercase;
    color: var(--brand-ink);
    white-space: nowrap;
  }
  .contact-icon {
    width: 15px;
    height: 15px;
    flex: none;
  }
</style>
</head>
<body>
<main class="canvas">
  <section class="card card-front" aria-label="Card front">
    <div class="wordmark"><span class="wordmark-dot"></span>BrightForge</div>
  </section>

  <section class="card card-back" aria-label="Card back">
    <div class="wordmark"><span class="wordmark-dot"></span>BrightForge</div>

    <div class="person">
      <p class="person-name">Tom Harcourt</p>
      <p class="person-role">Founder &amp; CTO</p>
    </div>

    <ul class="contact">
      <li class="contact-item">
        <svg class="contact-icon" viewBox="0 0 16 16" aria-hidden="true">
          <circle cx="8" cy="8" r="7" fill="none" stroke="#1ea0dc" stroke-width="1.2"/>
          <path d="M5.5 4.5 L7 6 L6.2 7 C6.8 8.3 7.7 9.2 9 9.8 L10 9 L11.5 10.5 L10.6 11.6 C7.5 11 5 8.5 4.4 5.4 Z" fill="#1ea0dc"/>
        </svg>
        +61 427 555123
      </li>
      <li class="contact-item">
        <svg class="contact-icon" viewBox="0 0 16 16" aria-hidden="true">
          <circle cx="8" cy="8" r="2.6" fill="none" stroke="#1ea0dc" stroke-width="1.4"/>
          <path d="M10.6 5.5 V9 C10.6 10.6 13.5 10.6 13.5 8 A5.5 5.5 0 1 0 10.5 12.9" fill="none" stroke="#1ea0dc" stroke-width="1.4"/>
        </svg>
        xxxx@brightforge.example
      </li>
      <li class="contact-item">
        <svg class="contact-icon" viewBox="0 0 16 16" aria-hidden="true">
          <circle cx="8" cy="8" r="7" fill="#1ea0dc"/>
        </svg>
        xxxxxharcourt
      </li>
      <li class="contact-item">
        <svg class="contact-icon" viewBox="0 0 16 16" aria-hidden="true">
          <rect x="1" y="1" width="14" height="14" rx="2" fill="#1ea0dc"/>
        </svg>
        tharcourt
      </li>
    </ul>
  </section>
</main>
</body>
</html>
```